Simple menu needed for Asian food truck

We are an Asian food truck that attends big festivals. Our menu is very simple featuring only about 5 or 6 dishes, but we need big pictures and lettering to capture the attention of festival goers. Our motto is "Fresh, Authentic, Homemade", it would be great to include that somewhere. We also need a menu that possibly magnetic so that we can easily take off items that are sold out, change pricing or add different dishes for specific venues. Attached is an example of what our current menu looks like.

```html
<!DOCTYPE html>
<html lang="en">
<head>
<meta charset="utf-8">
<title>Mei's Homestyle Egg Rolls – Food Truck Menu</title>
<link rel="stylesheet" href="https://fonts.googleapis.com/css2?family=Bebas+Neue&family=Oswald:wght@500;600&family=Kaushan+Script&family=Montserrat:wght@500&display=swap">
<style>
  :root {
    --page: #ffffff;
    --wood-dark: #140f0b;
    --wood-mid: #2c2119;
    --wood-warm: #3a2c21;
    --frame: #b58d45;
    --gold: #f6d37f;
    --script: #f2c64a;
    --orange: #d8772a;
    --orange-light: #f5b246;
    --herb: #6f9a3a;
    --white: #ffffff;
    --muted: #e9e2d6;
  }
  * { box-sizing: border-box; margin: 0; padding: 0; }
  html, body { width: 1200px; height: 1000px; overflow: hidden; background: var(--page); }
  .canvas { position: relative; width: 1200px; height: 1000px; }

  .menu-board {
    position: absolute; left: 278px; top: 80px; width: 642px; height: 840px;
    overflow: hidden; background: var(--wood-dark);
  }
  .wood-texture {
    position: absolute; inset: 0;
    background:
      radial-gradient(ellipse 70% 50% at 50% 45%, rgba(90,66,48,0.35), transparent 75%),
      linear-gradient(175deg, var(--wood-warm), var(--wood-mid) 40%, var(--wood-dark) 95%);
  }
  .plank-seams {
    position: absolute; inset: 0;
    background: repeating-linear-gradient(180deg, transparent 0 70px, rgba(0,0,0,0.35) 70px 72px);
  }
  .board-frame {
    position: absolute; left: 27px; top: 25px; width: 588px; height: 795px;
    border: 1px solid var(--frame); border-radius: 10px;
  }

  .brush-area {
    position: absolute; border-radius: 50%;
    background: radial-gradient(circle at center, var(--orange-light), rgba(216,119,42,0.75) 50%, rgba(216,119,42,0) 72%);
  }
  .brush-area.left { left: -60px; top: 720px; width: 200px; height: 200px; }
  .brush-area.right { left: 530px; top: 680px; width: 220px; height: 220px; }

  .herb-area {
    position: absolute; border-radius: 50%;
    background: radial-gradient(ellipse at center, rgba(111,154,58,0.55), rgba(111,154,58,0) 70%);
  }

  .brand {
    position: absolute; left: 50px; top: 62px; width: 145px; height: 145px;
    display: flex; align-items: center; justify-content: center; text-align: center;
  }
  .brand-mark { position: absolute; inset: 0; border-radius: 50%; border: 3px solid var(--orange); }
  .brand-name {
    font-family: 'Oswald', sans-serif; font-weight: 600; font-size: 21px;
    line-height: 1.08; color: var(--orange); letter-spacing: 1px;
  }

  .title {
    position: absolute; left: 214px; top: 56px; width: 386px;
    font-family: 'Bebas Neue', sans-serif; font-weight: 400; font-size: 60px; line-height: 1;
    color: var(--white); letter-spacing: 2.5px; text-align: center;
  }
  .motto {
    position: absolute; left: 214px; top: 108px; width: 386px; text-align: center;
    font-family: 'Kaushan Script', cursive; font-size: 27px; color: var(--script);
    letter-spacing: 0.6px;
  }

  .dish { position: absolute; text-align: center; }
  .dish-photo { position: absolute; border-radius: 8px; }
  .dish-name {
    position: absolute; left: 0; width: 100%;
    font-family: 'Oswald', sans-serif; font-weight: 600; font-size: 22px;
    line-height: 27px; color: var(--gold); letter-spacing: 0.5px;
  }
  .dish-note {
    position: absolute; left: 0; width: 100%;
    font-family: 'Oswald', sans-serif; font-weight: 500; font-size: 11.5px;
    line-height: 19px; color: var(--white); letter-spacing: 0.3px;
  }
  .price-badge {
    position: absolute; width: 68px; height: 68px; border-radius: 50%;
    background: var(--orange); color: var(--white);
    display: flex; flex-direction: column; align-items: center; justify-content: center;
    font-family: 'Oswald', sans-serif; font-weight: 600;
  }
  .price-badge .deal { font-size: 11px; line-height: 1; }
  .price-badge .amount { font-size: 29px; line-height: 1; }

  .site-link {
    position: absolute; left: 0; top: 780px; width: 642px; text-align: center;
    font-family: 'Montserrat', sans-serif; font-weight: 500; font-size: 13px;
    letter-spacing: 2px; color: var(--muted);
  }
</style>
</head>
<body>
<div class="canvas">
  <section class="menu-board">
    <div class="wood-texture" role="img" aria-label="Dark wooden plank background texture"></div>
    <div class="plank-seams"></div>

    <div class="herb-area" role="img" aria-label="Fresh parsley sprig" style="left:-20px; top:465px; width:100px; height:130px;"></div>
    <div class="herb-area" role="img" aria-label="Fresh parsley sprig" style="left:570px; top:295px; width:90px; height:90px;"></div>
    <div class="herb-area" role="img" aria-label="Fresh parsley sprig" style="left:545px; top:450px; width:110px; height:160px;"></div>

    <div class="brush-area left" role="img" aria-label="Orange brush stroke decoration"></div>
    <div class="brush-area right" role="img" aria-label="Orange brush stroke decoration"></div>
    <div class="board-frame"></div>

    <div class="brand">
      <div class="brand-mark"></div>
      <div class="brand-name">MEI'S<br>HOMESTYLE<br>EGG ROLLS</div>
    </div>
    <h1 class="title">FOOD TRUCK MENU</h1>
    <p class="motto">Fresh, authentic, Homemade</p>

    <div class="dish" style="left:70px; top:190px; width:240px; height:180px;">
      <div class="dish-photo" role="img" aria-label="Photo of three fried chicken egg rolls in a paper tray"
           style="left:32px; top:0; width:160px; height:120px; background:linear-gradient(150deg,#f3efe7,#d4a24c 55%,#b57a2e);"></div>
      <div class="price-badge" style="left:152px; top:57px;"><span class="deal">3 FOR</span><span class="amount">$6</span></div>
      <div class="dish-name" style="top:135px;">CHIKEN EGG ROLLS</div>
    </div>

    <div class="dish" style="left:70px; top:367px; width:240px; height:200px;">
      <div class="dish-photo" role="img" aria-label="Photo of two fresh shrimp spring rolls on a paper tray"
           style="left:30px; top:0; width:162px; height:123px; background:linear-gradient(150deg,#f4f2ee,#cfe0cf 50%,#f0a98f);"></div>
      <div class="price-badge" style="left:152px; top:64px;"><span class="deal">2 FOR</span><span class="amount">$6</span></div>
      <div class="dish-name" style="top:143px;">FRESH SPRINGROLLS</div>
      <div class="dish-note" style="top:170px;">(SHRIMP OR VEGGIE)</div>
    </div>

    <div class="dish" style="left:70px; top:568px; width:240px; height:200px;">
      <div class="dish-photo" role="img" aria-label="Photo of grilled Chinese BBQ pork skewers on a paper tray"
           style="left:12px; top:0; width:195px; height:122px; background:linear-gradient(150deg,#f2efea,#b83a4e 50%,#5a1a22);"></div>
      <div class="price-badge" style="left:137px; top:63px;"><span class="deal">2 FOR</span><span class="amount">$6</span></div>
      <div class="dish-name" style="top:141px;">CHINESE BBQ<br>PORK SKEWERS</div>
    </div>

    <div class="dish" style="left:312px; top:182px; width:240px; height:160px;">
      <div class="dish-photo" role="img" aria-label="Photo of fried rice with pork and peas in a paper tray"
           style="left:32px; top:0; width:183px; height:108px; background:linear-gradient(150deg,#efe6d2,#c9a66a 55%,#8a5a35);"></div>
      <div class="price-badge" style="left:176px; top:47px;"><span class="deal">BOWL</span><span class="amount">$5</span></div>
      <div class="dish-name" style="top:117px;">FRIED RICE</div>
      <div class="dish-note" style="top:139px;">(CHICKEN OR PORKK)</div>
    </div>

    <div class="dish" style="left:312px; top:358px; width:240px; height:200px;">
      <div class="dish-photo" role="img" aria-label="Photo of a fried stuffed chicken wing with a side of fried rice"
           style="left:20px; top:0; width:210px; height:87px; background:linear-gradient(150deg,#f4f2ef,#d9b070 55%,#c98a2c);"></div>
      <div class="price-badge" style="left:176px; top:45px;"><span class="deal">COMBO</span><span class="amount">$8</span></div>
      <div class="dish-name" style="top:104px;">ANGEL WING</div>
      <div class="dish-note" style="top:130px;">(STUFFED CHICKEN WING)<br>WITH SIDE OF FRIED RICE</div>
    </div>

    <div class="dish" style="left:312px; top:538px; width:240px; height:200px;">
      <div class="dish-photo" role="img" aria-label="Photo of three flavored iced teas in strawberry, mango and peach"
           style="left:60px; top:0; width:130px; height:132px; background:linear-gradient(90deg,#e9605a,#f3a52e 50%,#e9c23a);"></div>
      <div class="price-badge" style="left:176px; top:81px;"><span class="amount">$5</span></div>
      <div class="dish-name" style="top:152px;">FLAVORED TEA</div>
      <div class="dish-note" style="top:182px; font-size:12px;">STRAWBERRY, MANGO, OR PEACH</div>
    </div>

    <p class="site-link">www.meiseggrolls.com/menu</p>
  </section>
</div>
</body>
</html>
```